BRAVO Estate Steward

We require a website built for this company. Logo is also on the attached document. Some info on the company:<br/>To create a work class experience for our clients for property maintenance. A personalised service that deliver’s what landlords need...Quality work, on time and managed from start to finish.<br/>We do things different, our clients deal with one contact, a client manager who manages your maintenance task from start to finish. Our service allows our expert trades people to do what they do best and leave the management/organising to us!<br/>I have drafted up the layout of the web ... very brief at this stage however once we have more info we will add links and can collate more information and provide. <br/>We just want to get a layout of what you think the web should look like and can go from there.

```html
<!DOCTYPE html>
<html lang="en">
<head>
<meta charset="utf-8">
<title>BRAVO Estate Steward</title>
<link href="https://fonts.googleapis.com/css2?family=Poppins:wght@400;500;600;700&display=swap" rel="stylesheet">
<style>
:root{
  --yellow:#f5b800;
  --slate:#48525a;
  --ink:#222;
  --body:#555;
  --white:#fff;
  --line:#5c666e;
}
*{margin:0;padding:0;box-sizing:border-box}
html,body{width:1200px;height:3125px;overflow:hidden}
body{font-family:'Poppins',sans-serif;color:var(--body);background:var(--white);position:relative}
.abs{position:absolute}
.hero{left:0;top:0;width:1200px;height:449px;background:linear-gradient(180deg,#9a7e74 0%,#b79b90 40%,#c9bbb2 70%,#bfc3c2 100%)}
.brand{left:233px;top:26px;color:var(--white);font-weight:600;font-size:22px;line-height:26px;letter-spacing:.5px}
.brand small{display:block;font-size:13px;line-height:16px;font-weight:600}
.nav{left:609px;top:47px;display:flex;gap:0;font-size:10px;font-weight:600;color:var(--white);letter-spacing:.3px}
.nav span{margin-right:26px}
.nav .active{color:var(--yellow)}
.hero-title{left:0;top:200px;width:1200px;text-align:center;color:var(--white);font-weight:600;font-size:26px}
.hero-sub{left:300px;top:240px;width:600px;text-align:center;color:var(--white);font-weight:500;font-size:15.5px;line-height:22px}
.photo{display:block}
.about-img{left:233px;top:499px;width:357px;height:265px;background:linear-gradient(135deg,#d8d8d8,#8a8c90 60%,#3a3d44)}
.mark{display:inline-block;width:12px;height:5px;background:radial-gradient(circle,var(--yellow) 1px,transparent 1.5px) 0 0/3px 2.5px}
.about-head{left:626px;top:511px;font-size:11.5px;font-weight:600;color:var(--ink);display:flex;align-items:center;gap:14px}
.about-text{left:626px;top:548px;width:336px;font-size:10.5px;line-height:17.6px}
.team{left:0;top:809px;width:1200px;height:390px;background:linear-gradient(180deg,#7aa6d8 0%,#a9c7e6 45%,#c5ccd0 62%,#4d7fa7 72%,#1f5f8c 100%)}
.team h2{position:absolute;top:71px;width:100%;text-align:center;font-size:11.5px;font-weight:600;color:var(--ink)}
.team p{position:absolute;left:278px;top:106px;width:644px;text-align:center;font-size:10.5px;line-height:17.6px;color:#333}
.sec-head{left:0;width:1200px;text-align:center;font-size:11.5px;font-weight:600;color:var(--ink)}
.sec-head .mark{display:block;margin:0 auto 8px}
.tile{width:218px;height:153px}
.btn-outline{width:86px;height:29px;border:1px solid var(--yellow);color:var(--yellow);font-size:8.5px;font-weight:600;display:flex;align-items:center;justify-content:center}
.services{left:0;top:1867px;width:1200px;height:537px;background:var(--slate)}
.services .sec-head{color:var(--white);top:56px}
.card{position:absolute;width:232px;height:172px;background:var(--white);padding:20px 20px 0 20px}
.card-head{display:flex;align-items:center;gap:10px;height:40px;font-size:11.5px;font-weight:600;color:#3a3a3a;line-height:13px}
.card-head svg{flex:none}
.card p{margin-top:12px;font-size:9.2px;line-height:16.3px;color:#666}
.loans-img{left:341px;top:2451px;width:518px;height:250px;background:linear-gradient(90deg,#b85a4e 0%,#c4453c 35%,#6f7479 55%,#c7c4c1 100%)}
.loans-img h2{position:absolute;width:100%;top:112px;text-align:center;color:var(--white);font-size:17px;font-weight:600}
.loans-text{left:330px;top:2718px;width:540px;text-align:center;font-size:10px;line-height:18px;font-weight:500;color:var(--ink)}
.btn-solid{left:557px;top:2764px;width:86px;height:29px;background:var(--yellow);color:var(--white);font-size:8.5px;font-weight:600;display:flex;align-items:center;justify-content:center}
.footer{left:0;top:2843px;width:1200px;height:282px;background:var(--slate);color:#d6d9dc}
.f-brand{left:233px;top:50px;color:var(--white);font-weight:600;font-size:22px;line-height:26px}
.f-brand small{display:block;font-size:12px;line-height:15px}
.f-about{left:233px;top:114px;width:170px;font-size:9px;line-height:16.3px}
.f-col{font-size:9px;line-height:18.5px}
.f-col h4{font-size:9.5px;font-weight:600;color:var(--white);margin-bottom:10px;letter-spacing:.3px}
.f-contact div{display:flex;gap:10px;align-items:flex-start;margin-bottom:4px}
.f-rule{left:233px;top:230px;width:733px;height:1px;background:var(--line)}
.f-copy{left:233px;top:250px;font-size:8.5px}
.f-legal{left:760px;top:250px;width:206px;text-align:right;font-size:8.5px}
.mail-btn{left:1099px;top:191px;width:40px;height:40px;border-radius:50%;background:var(--yellow);display:flex;align-items:center;justify-content:center}
</style>
</head>
<body>

<header class="hero abs" role="img" aria-label="Aerial photo of a sandy beach with surf and red beach umbrellas">
  <div class="brand abs">BRAVO<small>Estate Steward</small></div>
  <nav class="nav abs">
    <span class="active">HOME</span><span>ABOUT US</span><span>SERVICES ▾</span><span>BENEFIT ▾</span><span>CONTACT US</span>
  </nav>
  <h1 class="hero-title abs">WELCOME TO THE FULL CIRCLE OF TRUST SERVICE</h1>
  <p class="hero-sub abs">BRAVO Estate Steward is a wealth management and financial advisory company with a strong commitment to the local community</p>
</header>

<div class="about-img abs" role="img" aria-label="Photo of two businessmen meeting at an office table"></div>
<h2 class="about-head abs"><span class="mark"></span>MEET MARCUS HALE</h2>
<p class="about-text abs">People, business, and property – these are Marcus’s three life passions. A business-minded child, he knew he wanted to be an entrepreneur at the age of 10. So an entrepreneur he became. He enjoyed successful careers in the money market, hospitality, and real estate before he discovered his true calling: property development. BRAVO Estate Group was born.</p>

<section class="team abs" role="img" aria-label="Photo of a coastal bay with rocky headland, beach and town">
  <h2>THE BRAVO TEAM</h2>
  <p>Marcus’s passion for property development is bolstered by a world-class team of property experts. He works with some of Australia’s best architects, builders, and designers to deliver outstanding results that exceed client expectations – every time. His team is loyal, experienced, and most importantly, dedicated to guiding you on your property journey.</p>
</section>

<h2 class="sec-head abs" style="top:1245px"><span class="mark"></span>PROJECTS</h2>
<div class="tile abs" style="left:244px;top:1304px;background:linear-gradient(135deg,#c9c6bf,#8f8d86 60%,#5d5a54)" role="img" aria-label="Photo of a bright living room with sofa and artwork"></div>
<div class="tile abs" style="left:490px;top:1304px;background:linear-gradient(180deg,#4a4a4a,#5b5b5b)" role="img" aria-label="Dark beach photo with project name lettering"></div>
<div class="tile abs" style="left:738px;top:1304px;background:linear-gradient(180deg,#2e4f86,#6b7a84 55%,#3d5a2e)" role="img" aria-label="Photo of a modern home at dusk with lit pool"></div>
<div class="btn-outline abs" style="left:557px;top:1485px">VIEW ALL</div>

<h2 class="sec-head abs" style="top:1554px"><span class="mark"></span>ACCOMMODATION</h2>
<div class="tile abs" style="left:244px;top:1614px;background:linear-gradient(135deg,#f1f0ee,#c8c6c2 50%,#7f8a6e)" role="img" aria-label="Photo of a white bedroom with garden view"></div>
<div class="tile abs" style="left:490px;top:1614px;background:linear-gradient(180deg,#5e86b8,#9aa9bb 45%,#d8c045)" role="img" aria-label="Photo of a blue weatherboard house with yellow fence"></div>
<div class="tile abs" style="left:738px;top:1614px;background:linear-gradient(180deg,#dfe3e6,#6f6a66 55%,#8a8a86)" role="img" aria-label="Photo of a modern apartment building on a street"></div>
<div class="btn-outline abs" style="left:557px;top:1794px">VIEW ALL</div>

<section class="services abs">
  <h2 class="sec-head abs"><span class="mark"></span>SERVICES</h2>
  <div class="card" style="left:234px;top:120px">
    <div class="card-head"><svg width="40" height="36" viewBox="0 0 40 36" fill="none" stroke="#666" stroke-width="2"><circle cx="13" cy="10" r="5"/><circle cx="27" cy="10" r="5"/><path d="M4 32v-6a9 9 0 0 1 18 0v6M18 32v-6a9 9 0 0 1 18 0v6"/></svg>Trade People</div>
    <p>Lorem ipsum dolor sit amet, consectetur adipiscing elit. Cras vitae orci lacinia dolor porta elementum vitae non nisl. Duis porttitor rutrum rhoncus. Orci varius natoque penatibus et magnis dis parturient montes</p>
  </div>
  <div class="card" style="left:484px;top:120px">
    <div class="card-head"><svg width="40" height="36" viewBox="0 0 40 36" fill="none" stroke="#666" stroke-width="2"><rect x="3" y="10" width="24" height="14"/><path d="M27 14h6l4 5v5h-10z"/><circle cx="10" cy="27" r="3"/><circle cx="31" cy="27" r="3"/></svg>Removalist Van and<br>Trailers</div>
    <p>Lorem ipsum dolor sit amet, consectetur adipiscing elit. Cras vitae orci lacinia dolor porta elementum vitae non nisl. Duis porttitor rutrum rhoncus. Orci varius natoque penatibus et magnis dis parturient montes</p>
  </div>
  <div class="card" style="left:734px;top:120px">
    <div class="card-head"><svg width="40" height="36" viewBox="0 0 40 36" fill="none" stroke="#666" stroke-width="2"><circle cx="20" cy="18" r="6"/><circle cx="20" cy="4" r="3"/><circle cx="20" cy="32" r="3"/><circle cx="5" cy="18" r="3"/><circle cx="35" cy="18" r="3"/><path d="M20 7v5M20 24v5M8 18h6M26 18h6"/></svg>Connections</div>
    <p>Lorem ipsum dolor sit amet, consectetur adipiscing elit. Cras vitae orci lacinia dolor porta elementum vitae non nisl. Duis porttitor rutrum rhoncus. Orci varius natoque penatibus et magnis dis parturient montes</p>
  </div>
  <div class="card" style="left:234px;top:311px">
    <div class="card-head"><svg width="40" height="36" viewBox="0 0 40 36" fill="none" stroke="#666" stroke-width="2"><rect x="4" y="4" width="32" height="12" rx="2"/><path d="M8 10h24M12 22l-2 4 2 4M20 22l-2 4 2 4M28 22l-2 4 2 4"/></svg>Smoke Alarms</div>
    <p>Lorem ipsum dolor sit amet, consectetur adipiscing elit. Cras vitae orci lacinia dolor porta elementum vitae non nisl. Duis porttitor rutrum rhoncus. Orci varius natoque penatibus et magnis dis parturient montes</p>
  </div>
  <div class="card" style="left:484px;top:311px">
    <div class="card-head"><svg width="40" height="36" viewBox="0 0 40 36" fill="none" stroke="#666" stroke-width="2"><rect x="3" y="9" width="34" height="24" rx="2"/><path d="M14 9V4h12v5M3 19h34"/></svg>Finance</div>
    <p>Lorem ipsum dolor sit amet, consectetur adipiscing elit. Cras vitae orci lacinia dolor porta elementum vitae non nisl. Duis porttitor rutrum rhoncus. Orci varius natoque penatibus et magnis dis parturient montes</p>
  </div>
  <div class="card" style="left:734px;top:311px">
    <div class="card-head"><svg width="40" height="36" viewBox="0 0 40 36" fill="none" stroke="#666" stroke-width="2"><path d="M4 14l7-8h18l7 8-16 18z M4 14h32M15 6l-3 8 8 18 8-18-3-8"/></svg>Wealth Creation</div>
    <p>Lorem ipsum dolor sit amet, consectetur adipiscing elit. Cras vitae orci lacinia dolor porta elementum vitae non nisl. Duis porttitor rutrum rhoncus. Orci varius natoque penatibus et magnis dis parturient montes</p>
  </div>
</section>

<div class="loans-img abs" role="img" aria-label="Photo of a couple receiving house keys"><h2>HOME LOANS</h2></div>
<p class="loans-text abs">Should you wish to consider our services, you can be assured of our commitment to your financial wellbeing now, and into the years ahead.</p>
<div class="btn-solid abs">CONTACT US</div>

<footer class="footer abs">
  <div class="f-brand abs">BRAVO<small>Estate Steward</small></div>
  <p class="f-about abs">We believe that everyone should have the right to enjoy a secure financial future and we are passionate about helping people make their goals and dreams become a reality.</p>
  <div class="f-col abs" style="left:430px;top:56px"><h4>QUICK LINKS</h4>Home<br>About Us<br>Services<br>Benefit<br>Contact Us</div>
  <div class="f-col abs" style="left:534px;top:56px"><h4>SERVICES</h4>Trade People<br>Removalist Van and Trailers<br>Connections<br>Smoke Alarms<br>Finance<br>Wealth Creation</div>
  <div class="f-col abs" style="left:687px;top:56px"><h4>BENEFIT</h4>Customer Service<br>Call Centre<br>Values<br>Pricing<br>Level of Expertise</div>
  <div class="f-col f-contact abs" style="left:796px;top:52px"><h4>CONTACT INFO</h4>
    <div><svg width="10" height="10" viewBox="0 0 10 10"><path d="M2 0l2 2-1 2 3 3 2-1 2 2-2 2C4 10 0 6 0 2z" fill="#fff"/></svg>02 5550 0142</div>
    <div><svg width="10" height="10" viewBox="0 0 10 10"><rect x="0" y="1.5" width="10" height="7" fill="#fff"/><path d="M0 2l5 3.5L10 2" stroke="#48525a" fill="none"/></svg>info@bravoestatesteward.com</div>
    <div><svg width="10" height="12" viewBox="0 0 10 12"><path d="M5 0a4 4 0 0 1 4 4c0 3-4 8-4 8S1 7 1 4a4 4 0 0 1 4-4z" fill="#fff"/><circle cx="5" cy="4" r="1.5" fill="#48525a"/></svg>4/18 Harbour Lane,<br>Seaview NSW</div>
  </div>
  <div class="mail-btn abs"><svg width="18" height="14" viewBox="0 0 18 14" fill="none" stroke="#fff" stroke-width="1.6"><rect x="1" y="1" width="16" height="12" rx="1.5"/><path d="M1 2l8 6 8-6"/></svg></div>
  <div class="f-rule abs"></div>
  <p class="f-copy abs">Copyright © 2019 BRAVO Estate Steward All rights reserved.</p>
  <p class="f-legal abs">Terms &amp; Conditions &nbsp;|&nbsp; Privacy Policy</p>
</footer>

</body>
</html>
```